Quenderix (www.quenderix-demo.net) needs exciting professional PowerPoint pitch template

Quenderix is an exciting new start-up targeting innovative ways to engage with retail customers at the point of sale.

Our customers are looking for us to help them increase the "wallet share" of their retail customers. The retail customer has their wallet open at the Point of Sale and are paying money to our customer. At Quenderix we are all about attracting the attention of the retail customer AT THAT POINT IN TIME and engaging the retail customer in spending a little more in that store or another store that has a relationship to the retail customer's purchase.

Our customers are the owners of very large supermarkets, chain stores, and financial institutions, and therefore when we pitch a proposal to these buyers it needs to be slick, professional, and very memorable.

The PowerPoint sales presentation template is a key part of striking that impression.

Here is some background...

Our Vision
Through applying new thinking to a mature industry we are reinventing selected segments of the Australian retail messaging business, generating significant value for our customers, our suppliers, and our owners.
We operate with integrity, agility, and intelligence to doing things smarter, faster and more efficiently.
We bring deep industry expertise, deep relationships with customers and suppliers, and a will to see the old ways give way to smarter ways – this is why we win.
From this economically sustainable platform, we will examine the disruption of other market segments by further leveraging the elements that make us successful.

Our Values
With our clients, with our suppliers, with our staff, and with our owners:
# We Partner – We align the interest of all stakeholders by striving to ensure everything we do is mutually beneficial and commercially sustainable in the long term. We are clear with all our stakeholders about what our expectations are of them, and we seek clarity from them in their expectations of us.
# We Innovate – In the segments we choose to compete in, we bring fresh ideas, new business processes, the right relationships, and the right technology to ensure the supply chain is nimble, competitive, and reliable.
# We are Accountable – We say what we will do, and then do what we say.
# We Perform – We use our skills, relationships, and reputation to deliver value to our customers, suppliers, and owners.

Initially we are building our business from low-tech through printing promotional offers and retailer messages on ATM and EFTPOS receipts, but as soon as cash flow supports it we will be engaging in high-tech real-time targeted offers to the specific consumer through video wall offers as people are at the checkout or walking through the shopping centre.

I'd like the PowerPoint template to reflect our vision and values.

The PowerPoint template will be used in communicating our proposals to our clients, and needs to catch and hold our audiences attention.

Please check out the web site we have just launched - it is pretty basic but it has only been up a week. We intend to sharpen it over the coming weeks, but you'll get the idea of what our core messages are.

I have recently sourced a logo from Sketchloft, plus business cards, and have attached the source files for your reference.
Updates

Hi everybody.  Thanks for the designs submitted so far.  Your submissions have helped me understand what I do and don't prefer, and I have updated the "Must Have/Nice to Have/Shouldn't Have" criteria accordingly.  I have also uploaded a powerpoint template that I had at a company I udsed to run that has the sort of visual theme I find appealing. I have more time to provide feedback now that the week is over, so I will comment on individual designs shortly, and I will respond to queries directed to me.

Kind Regards - Gareth

Target Market(s)

Our customers are large corporations that have professional Point Of Sale marketing experts looking for a supplier with an edge over others in a crowded market. The buyer of our product and services is ultimately a communications expert. They want to see distinctive competence, and an agility of thinking that will make them money through driving more consumer spending.

Industry/Entity Type

Financial

Font styles to use
Sans Serif

Colors
34a7d7
0892cd
3276b5

Requirements
Must have
• The following Slides: Title Slide, Agenda, About Quenderix, Thank you
The pages must be easy on the eye.
The final product must be a PowerPoint template file with the usual "Title", "Title and Content", "Title & Table", and "Blank" page types.
Widescreen format please.
Nice to have
• The pages should have an eye-catching visual element running through all the pages. I have attached a template from a company i used to be involved with that has a visual theme running through it that I like.
Plenty of whitespace - have a look at www.quenderix-demo.net.
Bonus points for pulling the text from the brief into the template.
Use "Innovation - Integrity - Service" as the tag line.
Should not have
• Pages should not be busy.
Stay away from too much black. I know the cards have black, but the presentation shouldn't.
I dont like serifed fonts. Use Blenvotz's Fjord Kit style for insporation.
The "Keeping Vivid" tag line was an invention of the logo designer that we do not want to cary forward. Please do not use it.

```html
<!DOCTYPE html>
<html lang="en">
<head>
<meta charset="utf-8">
<title>Quenderix Presentation Template</title>
<link rel="stylesheet" href="https://fonts.googleapis.com/css2?family=Graduate&family=Cinzel:wght@400;600&family=Open+Sans:wght@400;600;700&display=swap">
<style>
  :root {
    --canvas: #ffffff;
    --frame: #3a3a3a;
    --sky-light: #7fd0f2;
    --sky: #34a7d7;
    --brand: #0892cd;
    --brand-deep: #3276b5;
    --navy: #0b3f70;
    --teal-deep: #1b5d80;
    --ink: #2b2b2b;
    --muted: #4a4a4a;
  }
  * { box-sizing: border-box; margin: 0; padding: 0; }
  html, body {
    width: 1200px; height: 900px; overflow: hidden;
    background: var(--canvas);
  }
  .canvas { position: relative; width: 1200px; height: 900px; }

  .slide {
    position: absolute; left: 277px; width: 646px;
    border: 1px solid var(--frame); background: #fff;
  }
  .slide--cover { top: 50px; height: 370px; }
  .slide--content { top: 457px; height: 370px; }

  .cover-banner {
    position: absolute; left: 17px; top: 18px; width: 609px; height: 150px;
    background:
      radial-gradient(ellipse 60% 40% at 40% 60%, rgba(255,255,255,0.55), rgba(255,255,255,0) 70%),
      linear-gradient(100deg, var(--sky-light) 0%, #5cc0ee 35%, var(--sky) 65%, var(--brand-deep) 100%);
  }
  .accent-bar {
    position: absolute; left: 17px; top: 170px; width: 609px; height: 15px;
    background: linear-gradient(90deg, #74b9e6 0%, var(--brand) 50%, var(--teal-deep) 100%);
  }
  .corner-mark { position: absolute; left: 17px; width: 46px; height: 46px; }
  .slide--cover .corner-mark { top: 312px; }
  .slide--content .corner-mark { top: 311px; left: 16px; }

  .brand-name {
    position: absolute; right: 64px; top: 328px;
    font-family: "Open Sans", Arial, sans-serif; font-weight: 600;
    font-size: 21px; letter-spacing: -0.3px; color: var(--brand);
  }

  .content-header {
    position: absolute; left: 16px; top: 17px; width: 613px; height: 52px;
    display: flex; align-items: center; justify-content: center;
    background:
      radial-gradient(ellipse 50% 60% at 20% 90%, rgba(120,200,240,0.35), rgba(120,200,240,0) 70%),
      linear-gradient(90deg, #1a7cc0 0%, #155f9c 45%, var(--navy) 100%);
  }
  .content-header h1 {
    font-family: "Graduate", "Arial Black", sans-serif; font-weight: 400;
    font-size: 36px; color: #fff; letter-spacing: 1px;
  }
  .content-underbar {
    position: absolute; left: 16px; top: 73px; width: 613px; height: 5px;
    background: linear-gradient(90deg, #6fb4e2 0%, var(--brand) 50%, var(--teal-deep) 100%);
  }

  .content-body {
    position: absolute; left: 38px; top: 100px; width: 362px;
    font-family: "Cinzel", Georgia, serif; color: var(--muted);
  }
  .content-body h2 {
    font-weight: 400; font-size: 16px; color: var(--ink); margin-bottom: 8px;
  }
  .lead { display: flex; gap: 7px; width: 388px; margin-bottom: 6px; }
  .lead-arrow { flex: 0 0 21px; height: 20px; margin-top: 2px; }
  .content-body p {
    font-size: 4.8px; line-height: 6.9px; letter-spacing: 0.05px;
  }
  .content-body > p { margin-bottom: 6px; }

  .tagline {
    position: absolute; right: 21px; top: 348px;
    font-family: "Open Sans", Arial, sans-serif; font-size: 8px;
    letter-spacing: 1.6px; color: var(--muted);
  }
  .tagline strong { color: var(--brand); font-weight: 600; }
  .tagline .sep { color: var(--brand); padding: 0 3px; }
</style>
</head>
<body>
<main class="canvas">

  <section class="slide slide--cover" aria-label="Title slide">
    <div class="cover-banner" role="img" aria-label="Abstract blue light-wave banner artwork"></div>
    <div class="accent-bar"></div>
    <svg class="corner-mark" viewBox="0 0 46 46" aria-hidden="true">
      <polygon points="0,0 0,46 46,46" fill="#0b7cc6"/>
    </svg>
    <div class="brand-name">Quenderix</div>
  </section>

  <section class="slide slide--content" aria-label="Title and content slide">
    <header class="content-header"><h1>TITLE PAGE</h1></header>
    <div class="content-underbar"></div>

    <div class="content-body">
      <h2>Content Title</h2>
      <div class="lead">
        <svg class="lead-arrow" viewBox="0 0 21 20" aria-hidden="true">
          <polygon points="0,0 12,0 21,10 12,20 0,20 8,10" fill="#34a7d7"/>
        </svg>
        <p>Quenderix places timely offers on receipts at the point of sale, reaching shoppers while their wallets are open. Our messages help retailers lift basket size and build lasting links with partner stores. We plan every campaign with care, measure every result, and share clear reports so each client sees real value from each printed receipt. Offers run on ATM and EFTPOS slips today, and soon on video walls at the checkout, so every message meets the shopper at the right moment in the right store.</p>
      </div>
      <p>Quenderix places timely offers on receipts at the point of sale, reaching shoppers while their wallets are open. Our messages help retailers lift basket size and build lasting links with partner stores. We plan every campaign with care, measure every result, and share clear reports so each client sees real value from each printed receipt. Offers run on ATM and EFTPOS slips today, and soon on video walls at the checkout, so every message meets the shopper at the right moment in the right store.</p>
      <p>Quenderix places timely offers on receipts at the point of sale, reaching shoppers while their wallets are open. Our messages help retailers lift basket size and build lasting links with partner stores. We plan every campaign with care, measure every result, and share clear reports so each client sees real value from each printed receipt. Offers run on ATM and EFTPOS slips today, and soon on video walls at the checkout, so every message meets the shopper at the right moment in the right store.</p>
      <p>Quenderix places timely offers on receipts at the point of sale, reaching shoppers while their wallets are open. Our messages help retailers lift basket size and build lasting links with partner stores. We plan every campaign with care, measure every result, and share clear reports so each client sees real value from each printed receipt. Offers run on ATM and EFTPOS slips today, and soon on video walls at the checkout, so every message meets the shopper at the right moment in the right store.</p>
    </div>

    <svg class="corner-mark" viewBox="0 0 46 46" aria-hidden="true">
      <polygon points="0,0 0,46 46,46" fill="#0b7cc6"/>
    </svg>
    <p class="tagline">Innovation<span class="sep">|</span><strong>Integrity</strong><span class="sep">|</span>Service</p>
  </section>

</main>
</body>
</html>
```